Website Design for NYC Female Attorney – Clean, Warm, Professional

Marian Thorpe, Esq.
www.MarianJThorpeLegal.example

I’m a New York City-based attorney and CPA with a reputation for providing thoughtful, high-integrity legal guidance in both estate planning and small business law. I’ve served over 500 clients, and maintain a perfect 5-star rating. Clients come to me for clarity, compassion, and results — and I want my new website to reflect that.

**🎯 WHAT I NEED:**
A clean, modern, and emotionally resonant website that highlights who I am, what I do, and why clients trust me. It must feel approachable and warm, but still professional and elegant — think Quillo meets boutique law firm. Feminine but not frilly.

**🧩 CORE WEBSITE SECTIONS (Top Navigation):**

1. **Home** – Strong first impression, tagline, CTA (book a call)
Homepage Copy (Sample Layout)
Headline:
Trusted Legal Guidance for Families and Founders.

Subheading:
Whether you’re protecting what you’ve built or building what’s next, I help you navigate estate planning and business law with confidence, compassion, and clarity.

Tagline (beneath logo or footer):
Legal Clarity for Life and Business.
2. **About Marian** – Bio, personal approach, credentials
3. **Services**

* *Estate Planning*
* *Business Law*
4. **Who I Work With** – Ideal clients (parents, entrepreneurs, etc.)
5. **Testimonials** – Client praise and social proof
6. **Success Stories** – Highlighting wins and case types
7. **FAQs** – Warm and clear answers to common questions
8. **Blog** – Thought leadership and helpful tips
8.5 Events
9. **Contact / Book a Call** – Scheduling or contact form

**🖼 STYLE DIRECTION:**

* Clean white backgrounds, soft jewel tones or neutrals
* Professional headshots and personal branding assets available
* Emphasis on readability, trust, and ease of navigation - THIS NEEDS TO BE BUILT OUT SO IT IS TRUSTED BY AI!
* No harsh colors, no corporate/legal clichés (e.g., gavels or scales) - I MEAN THIS. I DO NOT WANT A BORING LAW WEBSITE WITH SCALES AND GAVELS
* Feminine edge (not pink-heavy), with strong hierarchy and callouts

**💡 DESIGN NOTES:**

* Mobile-first design required
* Should include space for video or welcome message
* Easy to update blog or CMS area preferred
* Built in a user-friendly platform like WordPress, Webflow, or similar
* Needs to feel elevated enough to support high-end flat fee packages

**📣 TONE:**
Smart. Warm. Sophisticated. Human.

**⚖️ FINAL DELIVERABLES:**

* Homepage + 5+ interior pages
* Desktop + mobile views
* Style guide (fonts, colors, buttons)
* Bonus if you can help with copy layout/structure (not just visuals)

**📍TARGET AUDIENCE:**

* Busy professionals and families in NYC
* Women and couples who want peace of mind
* Entrepreneurs and creatives needing solid legal support

Here is my current site: www.MarianJThorpeLegal.example
And here is a second business I have: www.QuickCounselDaily.example

Families and business owners

Law

Serif
Sans Serif
Script

• This website must be built to be seen as trustworthy by AI.

```html
<!DOCTYPE html>
<html lang="en">
<head>
<meta charset="utf-8">
<title>Law Office of Marian Thorpe</title>
<link href="https://fonts.googleapis.com/css2?family=Instrument+Serif:ital@0;1&family=Inter:ital,wght@0,300;0,400;0,500;1,300;1,400&display=swap" rel="stylesheet">
<style>
:root{
  --maroon:#3a1113;
  --canvas:#ece8e1;
  --white:#ffffff;
  --soft:#f5f2ee;
  --tag:#efe8e2;
  --ink:#2b1a1a;
  --muted:#6f6363;
  --line:#d9d0c9;
  --star:#f2a23c;
  --quote:#c6a096;
}
*{box-sizing:border-box;margin:0;padding:0}
html,body{width:1200px;height:4135px;overflow:hidden}
body{background:var(--canvas);font-family:"Inter",sans-serif;color:var(--ink);position:relative}
.abs{position:absolute}
.page{position:absolute;left:85px;top:80px;width:1030px;height:3973px;background:var(--white)}
.serif{font-family:"Instrument Serif",serif;font-weight:400;text-transform:uppercase;letter-spacing:-.01em;color:var(--maroon)}
.serif u{text-decoration-thickness:1px;text-underline-offset:5px}
.tag{position:absolute;height:22px;padding:0 16px;border-radius:11px;background:var(--tag);font-size:10.5px;line-height:22px;color:var(--ink)}
.btn{position:absolute;height:26px;border-radius:13px;background:var(--maroon);color:#fff;font-size:10.5px;line-height:26px;padding-left:16px;padding-right:34px;white-space:nowrap}
.btn::after{content:"↗";position:absolute;right:3px;top:3px;width:20px;height:20px;border-radius:50%;background:#fff;color:var(--maroon);font-size:10px;line-height:20px;text-align:center}
.btn.light{background:#fff;color:var(--ink);border:1px solid var(--line)}
.btn.light::after{background:var(--maroon);color:#fff}
.btn.onDark{background:#fff;color:var(--maroon)}
.btn.onDark::after{background:var(--maroon);color:#fff}
.stars{color:var(--star);letter-spacing:4px}
/* hero */
.hero-photo{left:85px;top:80px;width:1030px;height:520px;background:linear-gradient(90deg,#6b5a52 0%,#3d2a24 45%,#1c1412 100%)}
.hero-band{left:85px;top:80px;width:322px;height:66px;background:var(--maroon)}
.hero-panel{left:85px;top:145px;width:536px;height:455px;background:linear-gradient(160deg,#f7f6f5 0%,#e4e2e1 60%,#cfcdcc 100%);border-bottom-right-radius:64px}
.logo{color:#fff;font-family:"Instrument Serif",serif;font-size:12px;letter-spacing:.12em;text-transform:uppercase;text-align:center}
.nav{left:406px;top:80px;width:709px;height:32px;background:#fff;border-bottom-left-radius:22px}
.nav a{position:absolute;top:9px;font-size:11.5px;color:var(--ink);text-decoration:none}
.badge{left:908px;top:284px;width:115px;height:189px;background:#fff;border-radius:10px}
.badge span{position:absolute;left:28px;width:60px;height:30px;border-radius:6px;background:#ece4df}
.stat{position:absolute;top:648px;width:247px;height:172px;background:var(--soft);border-radius:8px}
.stat .lbl{position:absolute;left:28px;top:38px;font-size:14px}
.stat .lbl::before{content:"";position:absolute;left:0;top:-15px;width:7px;height:7px;border-radius:50%;background:var(--maroon)}
.stat .num{position:absolute;right:24px;bottom:18px;font-size:44px}
.check{position:absolute;left:213px;font-size:14.5px}
.check::before{content:"✓";margin-right:9px;font-weight:500}
.svc-img{position:absolute;top:1529px;width:378px;height:362px;border-radius:6px}
.svc-card{position:absolute;background:#fff;border-radius:8px;padding:18px 22px}
.svc-card h3{font-weight:400;font-size:17px;margin-bottom:10px}
.svc-card li{font-size:9.5px;color:var(--muted);line-height:16px;margin-left:10px}
.svc-card i{position:absolute;right:18px;top:18px;width:20px;height:20px;border-radius:50%;background:var(--maroon);color:#fff;font-style:normal;font-size:9px;line-height:20px;text-align:center}
.blog{position:absolute;top:2852px;width:247px;height:228px;border-radius:6px;padding:30px 25px}
.blog h4{font-weight:400;font-size:15px;line-height:23px}
.blog p{margin-top:52px;font-size:9.5px;color:var(--muted);line-height:16px}
.author{position:absolute;left:25px;top:176px}
.author span{position:absolute;left:0;top:0;width:32px;height:32px;border-radius:50%;background:linear-gradient(135deg,#b59a8c,#5c4038)}
.author b{position:absolute;left:44px;top:2px;font-weight:400;font-size:12px;white-space:nowrap}
.author em{position:absolute;left:44px;top:18px;font-style:normal;font-size:10px;color:var(--muted);white-space:nowrap}
.field{position:absolute;width:225px;border-bottom:1px solid var(--line);height:34px;font-size:13px;color:var(--ink);padding-top:4px}
.fcol h5{font-family:"Instrument Serif",serif;font-weight:400;font-size:17px;text-transform:uppercase;color:var(--maroon);margin-bottom:10px}
.fcol p{font-size:11.5px;color:var(--muted);line-height:27px}
</style>
</head>
<body>
<div class="page"></div>

<!-- hero -->
<div class="abs hero-photo" role="img" aria-label="Portrait of the attorney in a dark blazer in front of a library"></div>
<div class="abs hero-panel"></div>
<div class="abs hero-band"></div>
<div class="abs logo" style="left:205px;top:110px;width:100px">Marian Thorpe</div>
<nav class="abs nav">
  <a style="left:112px">Home</a><a style="left:191px">About Marian</a><a style="left:279px">Services</a><a style="left:366px">Testimonials</a><a style="left:444px">FAQs</a><a style="left:500px">Blog</a><a style="left:561px">Events</a>
</nav>
<div class="btn light" style="left:879px;top:127px">Contact Us</div>
<div class="abs badge"><span style="top:22px"></span><span style="top:78px"></span><span style="top:134px"></span></div>
<div class="abs" style="left:1038px;top:523px;width:34px;height:34px;border-radius:50%;background:#fff;color:var(--maroon);text-align:center;line-height:34px;font-size:14px">↓</div>
<h1 class="abs serif" style="left:213px;top:210px;font-size:39px;line-height:49px">Trusted Legal<br><u>Guidance for Families</u><br>and Founders.</h1>
<p class="abs" style="left:213px;top:366px;width:380px;font-size:11px;line-height:19px">Whether You're Protecting What You've Built Or Building What's Next, I Help You Navigate Estate Planning And Business Law With Confidence, Compassion, And Clarity.</p>
<div class="btn" style="left:213px;top:444px">Book A Call</div>
<div class="abs" style="left:213px;top:495px;font-size:13px;font-weight:500"><span class="stars" style="font-size:18px">★★★★★</span> 5 STAR RATING</div>

<!-- stats -->
<div class="stat" style="left:213px"><div class="lbl">Clients Served</div><div class="num serif">500+</div></div>
<div class="stat" style="left:476px"><div class="lbl">Average Rating</div><div class="num serif">5-Star</div></div>
<div class="stat" style="left:739px"><div class="lbl">Legal Experience</div><div class="num serif">10+</div></div>

<!-- about -->
<div class="tag" style="left:213px;top:915px">Our About Us</div>
<h2 class="abs serif" style="left:338px;top:903px;font-size:36px">Meet <u>Marian</u></h2>
<p class="abs" style="left:213px;top:962px;width:320px;font-size:10px;line-height:18.5px;color:var(--muted)">I'm Marian Thorpe, An Attorney And CPA Based In New York City. I've Helped Over 500 Clients Protect Their Families And Businesses With Thoughtful, Practical, And High-Integrity Legal Guidance. I Believe Great Legal Counsel Combines Clarity With Compassion — And I'm Here To Make The Complex Feel Simple And Stress-Free.</p>
<div class="check" style="top:1097px">JD And CPA — Trusted Dual Expertise</div>
<div class="check" style="top:1133px">Perfect 5-Star Client Rating</div>
<div class="check" style="top:1169px">Focused On Real Results, Not Jargon</div>
<div class="check" style="top:1205px">Modern, Boutique, Client-First Approach</div>
<div class="btn" style="left:213px;top:1254px">Learn More About Us</div>
<div class="abs" role="img" aria-label="Photo of the attorney seated on a cream sofa in a bright office" style="left:568px;top:911px;width:418px;height:372px;border-radius:6px;background:linear-gradient(120deg,#f3f0ec 0%,#ddd5cc 55%,#b8a89a 100%)"></div>

<!-- services -->
<div class="abs" style="left:85px;top:1375px;width:1030px;height:588px;background:var(--soft)"></div>
<div class="tag" style="left:213px;top:1450px;background:#fff">Our Services</div>
<h2 class="abs serif" style="left:351px;top:1438px;font-size:36px">How I Can <u>Help</u></h2>
<div class="btn" style="left:852px;top:1448px">Scheduling Now</div>
<div class="svc-img" style="left:213px;background:linear-gradient(135deg,#efe3d2,#cdbfae 60%,#8e8577)" role="img" aria-label="Model house on estate planning documents"></div>
<div class="svc-img" style="left:608px;background:linear-gradient(135deg,#e9e6e3,#a9a29c 55%,#3e3532)" role="img" aria-label="Hands signing a business contract at a desk"></div>
<div class="svc-card" style="left:229px;top:1752px;width:350px;height:125px"><h3>Estate Planning</h3><i>↗</i><ul><li>Wills &amp; Trusts, Advance Directives, And Guardianship Planning.</li><li>Protect Your Family's Future With Clear, Legally Sound Documents.</li></ul></div>
<div class="svc-card" style="left:624px;top:1780px;width:305px;height:97px"><h3>Business Law</h3><i>↗</i><ul><li>Entity Formation, Contracts, Compliance.</li><li>Build And Protect Your Business With Confidence.</li></ul></div>

<!-- testimonials -->
<div class="tag" style="left:213px;top:2058px">Our Testimonials</div>
<h2 class="abs serif" style="left:395px;top:2046px;font-size:36px">What Our <u>Client</u> Says</h2>
<div class="btn" style="left:826px;top:2056px">View All Testimonials</div>
<div class="abs" style="left:211px;top:2118px;font-family:'Instrument Serif',serif;font-size:140px;line-height:140px;color:var(--quote)">“</div>
<div class="abs stars" style="left:213px;top:2222px;font-size:22px">★★★★★</div>
<div class="abs" style="left:213px;top:2258px;font-size:13px;color:var(--muted)">5 Star Rating</div>
<p class="abs" style="left:395px;top:2130px;width:590px;font-style:italic;font-weight:300;font-size:16.5px;line-height:27.5px">"Lorem Ipsum Dolor Sit Amet Consectetur. Elementum Molestie Eget Posuere Elementum Pretium Risus Vehicula Facilisis. Pulvinar Nisl Elementum Scelerisque Gravida Id Pulvinar Gravida. In Feugiat Venenatis Pellentesque Ultricies Leo. Lacus Diam Etiam Rutrum Malesuada. Ultrices Felis Quam Ut Sed. Cras Felis Quis Quis."</p>
<div class="abs" style="left:213px;top:2339px;width:667px;height:1px;background:var(--line)"></div>
<div class="abs" style="left:912px;top:2324px;width:30px;height:30px;border-radius:50%;background:var(--tag);text-align:center;line-height:30px;font-size:12px">←</div>
<div class="abs" style="left:955px;top:2324px;width:30px;height:30px;border-radius:50%;background:var(--maroon);color:#fff;text-align:center;line-height:30px;font-size:12px">→</div>

<!-- events band -->
<div class="abs" style="left:146px;top:2446px;width:908px;height:236px;border-radius:12px;background:var(--maroon)"></div>
<h2 class="abs serif" style="left:213px;top:2517px;font-size:36px;line-height:49px;color:#fff">Stay <u>Connected</u> Learn<br>Together</h2>
<p class="abs" style="left:693px;top:2515px;width:300px;font-size:10.5px;line-height:18.5px;color:#e7d8d6">Join My Upcoming Estate Planning Workshops And Small Business Q&amp;A Sessions Designed To Empower, Educate, And Connect.</p>
<div class="btn onDark" style="left:816px;top:2584px">View Upcoming Events</div>

<!-- blogs -->
<div class="tag" style="left:213px;top:2778px">Our Blogs</div>
<h2 class="abs serif" style="left:335px;top:2766px;font-size:36px">Insights &amp; <u>Resources</u></h2>
<div class="btn" style="left:864px;top:2776px">View All Blogs</div>
<div class="blog" style="left:213px"><h4>Lorem Ipsum Dolor Amet Molestie Posuere</h4><p>Lorem Ipsum Dolor Sit Amet Consectetur Elit Est Nam Malesuada.</p><div class="author"><span></span><b>Nora Ellis</b><em>Assistant Director</em></div></div>
<div class="blog" style="left:476px;background:var(--soft)"><h4>Lorem Ipsum Dolor Amet Molestie Posuere</h4><p>Lorem Ipsum Dolor Sit Amet Consectetur Elit Est Nam Malesuada.</p><div class="author"><span></span><b>Nora Ellis</b><em>Assistant Director</em></div></div>
<div class="blog" style="left:739px"><h4>Lorem Ipsum Dolor Amet Molestie Posuere</h4><p>Lorem Ipsum Dolor Sit Amet Consectetur Elit Est Nam Malesuada.</p><div class="author"><span></span><b>Nora Ellis</b><em>Assistant Director</em></div></div>

<!-- contact -->
<div class="tag" style="left:213px;top:3178px">Our Contact Us</div>
<h2 class="abs serif" style="left:364px;top:3166px;font-size:36px">Get In <u>Touch</u></h2>
<p class="abs" style="left:215px;top:3236px;width:480px;font-size:11px;line-height:20px;color:var(--muted)">Lorem Ipsum Dolor Sit Amet Consectetur. Vestibulum Purus Consequat Lectus Natoque Donec Fringilla. Porta Non Urna Tristique Magna Eleifend. Vulputate Sed Enim Feugiat Sed Volutpat Nisi Euismod Tellus.</p>
<div class="field" style="left:215px;top:3320px">First Name</div>
<div class="field" style="left:456px;top:3320px">Last Name</div>
<div class="field" style="left:215px;top:3378px">Email</div>
<div class="field" style="left:456px;top:3378px">Address</div>
<div class="field" style="left:215px;top:3436px">Services</div>
<div class="field" style="left:456px;top:3436px">Date</div>
<div class="btn" style="left:215px;top:3501px">Contact Us</div>
<div class="abs" role="img" aria-label="Standing portrait of the attorney in a dark dress" style="left:715px;top:3173px;width:270px;height:356px;background:linear-gradient(180deg,#f1eeea 0%,#e4dcd5 60%,#cfc3b9 100%)"></div>

<!-- footer -->
<div class="abs" style="left:85px;top:3620px;width:1030px;height:433px;background:var(--soft)"></div>
<h2 class="abs serif" style="left:213px;top:3654px;font-size:27px">Join My Legal <u>Insights List</u></h2>
<div class="abs" style="left:600px;top:3654px;width:383px;height:32px;border-radius:16px;background:#fff;font-size:10.5px;line-height:32px;padding-left:18px">Enter Your Email</div>
<div class="btn" style="left:853px;top:3657px">Subscribe Now</div>
<div class="abs" style="left:213px;top:3715px;width:772px;height:1px;background:var(--line)"></div>
<div class="abs" style="left:213px;top:3798px;font-family:'Instrument Serif',serif;font-size:22px;letter-spacing:.12em;text-transform:uppercase;color:var(--maroon)">Marian Thorpe</div>
<div class="abs" style="left:213px;top:3850px;font-family:'Instrument Serif',serif;font-size:16px;color:var(--ink)">Legal Clarity For Life And Business.</div>
<p class="abs" style="left:213px;top:3886px;width:250px;font-size:11px;line-height:19px;color:var(--muted)">Lorem Ipsum Dolor Sit Amet Consectetur. Magna Risus Maecenas Pulvinar Interdum Tincidunt Faucibus. Risus .</p>
<div class="abs fcol" style="left:520px;top:3758px"><h5>Links</h5><p>Home<br>About Marian<br>Services<br>Testimonials<br>FAQs<br>Blog<br>Events</p></div>
<div class="abs fcol" style="left:659px;top:3758px;width:200px"><h5>Contact Us</h5><p style="line-height:19px;margin-top:6px">48 Alder Street, Fl 9 New<br>York, NY 10002</p><p>marian@marianjthorpelegal.example<br>(212) 555-0148</p></div>
<div class="abs fcol" style="left:893px;top:3758px"><h5>About Us</h5><p style="line-height:22px">Out Story<br>Blogs<br>Success Stories</p></div>
<div class="abs" style="left:213px;top:4018px;width:772px;height:1px;background:var(--line)"></div>
<div class="abs" style="left:213px;top:4027px;font-size:9.5px;color:var(--muted)">Copyright © 2025 Law Office Of Marian Thorpe . All Rights Reserved.</div>
<div class="abs" style="left:825px;top:4027px;font-size:9.5px;color:var(--muted)">Privacy Policy &amp; Terms Of Condition</div>
</body>
</html>
```